Web re-design project www.vempresoft.com

We need a corporate website for a startup company called Vempre Labs. The company offers web-based worksite management system for big construction companies. In short, replacing annoying papers with iPads.
We need the site main page to provide basic overview of the company and then inner page layout for displaying news and detailed information about products.
Currently we have a site up at:
http://www.vempresoft.com/en/main
but as you can see the graphic design is a bit lacking in quality(implemented by a tech guy :)
We need you to pimp that web site design up!
There is possibility for more freelance work in the future related to our web products, slide show designs and printed marketing materials.
Our main product is LOMVI. You can find a short presentation about what it does here:
http://www.vempresoft.com/en/lomvi
Here you can find packages of images and screenshots related to our company:
https://files.plimbox.net/u/7719026/vempre_images.zip
https://files.plimbox.net/u/7719026/vempresoft%20images2.zip
Product logo svg can be found here:
https://files.plimbox.net/u/7719026/LOMVI-logo.svg
Your are not forced to use those images, but hopefully there will be something that is useful.
Hope to hear from you guys soon!
Cheers,
Ossi
Update:
We will be using LOMVI logo as the company brand. I don't like our current Vempre Labs company logo, so that doesn't need to be included in the site design.
Update 2:
I like website designs that are "light", elegant and pretty simplistic. One example is our product login page (screenshot included in files).
Update 3:
Sites from the same industry / type of products:
http://www.rakmoda.fi/
http://www.quarvelgrid.com/products/software/network-applications/fieldsync-3d
http://www.dornvex.com/construction/heavy-civil/software-solutions/Linked-Network.aspx?dtID=overview&
Target audience for the website is companies in the construction sector, and possibly corporate investors
Graphic Design

```html
<!DOCTYPE html>
<html lang="en">
<head>
<meta charset="utf-8">
<title>LOMVI – Worksite management</title>
<link rel="stylesheet" href="https://fonts.googleapis.com/css2?family=Open+Sans:wght@400;600&family=Lato:wght@300;400;700&family=PT+Sans+Narrow:wght@400;700&display=swap">
<style>
  :root {
    --ink: #1c1c1c;
    --text: #6a6a6a;
    --muted: #8c8c8c;
    --accent: #c4161c;
    --nav-top: #4a4a4a;
    --nav-bottom: #1e1e1e;
    --panel: rgba(40, 40, 40, 0.86);
    --rule: #e4e4e4;
  }
  * { box-sizing: border-box; margin: 0; padding: 0; }
  html, body { width: 1009px; height: 1200px; overflow: hidden; }
  body {
    position: relative;
    background: #fff;
    font-family: "Lato", sans-serif;
    color: var(--text);
  }
  a { text-decoration: none; color: inherit; }

  .page-band {
    position: absolute; left: 0; right: 0; top: 148px; height: 420px;
    background: linear-gradient(#ececec, #f6f6f6 80%, #fff);
  }

  /* header */
  .brand {
    position: absolute; left: 34px; top: 26px;
    display: flex; align-items: center; gap: 12px;
  }
  .brand-dot { width: 30px; height: 30px; border-radius: 50%; background: var(--accent); }
  .brand-name {
    font-family: "Open Sans", sans-serif; font-weight: 400;
    font-size: 37px; letter-spacing: 1px; color: var(--ink); line-height: 1;
  }
  .search {
    position: absolute; left: 751px; top: 62px; width: 218px; height: 25px;
    border: 1px solid #dcdcdc; border-radius: 2px; background: #fff;
    display: flex; align-items: center;
  }
  .search-input { flex: 1; font-size: 11px; color: #555; padding-left: 11px; }
  .search-btn {
    width: 26px; height: 100%; border-left: 1px solid #dcdcdc;
    display: flex; align-items: center; justify-content: center;
  }

  /* navigation */
  .main-nav {
    position: absolute; left: 31px; top: 103px; width: 944px; height: 45px;
    background: linear-gradient(var(--nav-top), #2c2c2c 50%, var(--nav-bottom));
    border-radius: 2px 2px 0 0;
    display: flex;
  }
  .main-nav a {
    font-family: "Open Sans", sans-serif; font-size: 14px; color: #fff;
    display: flex; align-items: center; padding: 0 30px;
    border-right: 1px solid #5a5a5a;
  }
  .main-nav a:first-child { padding-left: 31px; }
  .main-nav a:last-child { border-right: none; }

  /* hero */
  .hero {
    position: absolute; left: 31px; top: 148px; width: 944px; height: 387px;
    background: #fff; padding: 7px 10px 10px;
    box-shadow: 0 14px 14px -10px rgba(0,0,0,0.18);
  }
  .hero-photo {
    position: relative; width: 926px; height: 370px;
    background: linear-gradient(100deg, #8a7b6e 0%, #a39283 25%, #c2c24a 45%, #6f6a66 65%, #9b8f86 100%);
  }
  .hero-panel {
    position: absolute; right: 0; top: 0; width: 300px; height: 100%;
    background: var(--panel); padding: 42px 22px 0 31px; color: #fff;
  }
  .hero-kicker { font-family: "PT Sans Narrow", sans-serif; font-weight: 700; font-size: 23px; line-height: 1.1; }
  .hero-title { font-family: "PT Sans Narrow", sans-serif; font-weight: 700; font-size: 32px; line-height: 1.1; margin-bottom: 18px; }
  .hero-panel p { font-size: 11.5px; font-weight: 700; line-height: 18.5px; margin-bottom: 9px; }
  .hero-cta {
    display: inline-block; margin-top: 4px; background: #000; color: #fff;
    font-family: "PT Sans Narrow", sans-serif; font-size: 13.5px; padding: 4px 12px;
  }
  .hero-dots { display: flex; gap: 4px; margin-top: 18px; margin-left: 9px; }
  .hero-dots span { width: 9px; height: 9px; border-radius: 50%; background: #fff; }

  /* content */
  .section-title {
    font-family: "Open Sans", sans-serif; font-size: 18.5px; color: var(--accent);
    font-weight: 400; line-height: 1;
  }
  .more {
    font-family: "PT Sans Narrow", sans-serif; font-weight: 700;
    font-size: 12.5px; color: var(--accent); display: inline-block; line-height: 1;
  }

  .latest { position: absolute; left: 33px; top: 569px; width: 652px; }
  .latest .section-title { height: 28px; }
  .news-item { display: flex; gap: 15px; height: 183px; }
  .news-item:last-child { height: 140px; }
  .news-thumb {
    flex: none; width: 186px; height: 111px; background: #fff;
    border: 1px solid #eee; box-shadow: 0 0 4px rgba(0,0,0,0.12); padding: 8px;
  }
  .news-thumb div { width: 100%; height: 100%; }
  .thumb-workers { background: linear-gradient(135deg, #cfcac2, #8c8378 60%, #b8b2a8); }
  .thumb-bridge { background: linear-gradient(180deg, #5b86c8, #aacbe8 55%, #d9dde0); }
  .thumb-site { background: linear-gradient(90deg, #2f5fa6, #c9c24b 50%, #3a66ad); }
  .news-body { width: 455px; padding-top: 2px; }
  .news-headline { font-size: 12.5px; color: #333; font-weight: 400; line-height: 16px; margin-bottom: 6px; }
  .news-body p { font-size: 10.2px; line-height: 18.5px; margin-bottom: 4px; letter-spacing: -0.1px; }
  .news-body .more { margin-top: 6px; }

  .divider { position: absolute; left: 707px; top: 570px; width: 1px; height: 495px; background: var(--rule); }

  .viewed { position: absolute; left: 725px; top: 569px; width: 252px; }
  .viewed .section-title { height: 38px; }
  .viewed-item { height: 118px; }
  .viewed-date { font-size: 11px; color: #444; line-height: 16px; margin-bottom: 2px; }
  .viewed-item p { font-size: 10px; line-height: 18.5px; letter-spacing: -0.1px; }
  .viewed-item .more { color: #555; font-size: 11px; margin-top: 7px; }

  /* footer */
  .site-footer {
    position: absolute; left: 0; right: 0; top: 1118px; height: 82px;
    background: linear-gradient(#ececec, #fff 18px);
  }
  .copyright { position: absolute; left: 31px; top: 27px; font-size: 10.5px; color: var(--muted); }
  .touch { position: absolute; right: 34px; top: 22px; display: flex; align-items: center; gap: 6px; font-size: 12.5px; color: #555; }
  .touch-circle { width: 16px; height: 16px; border-radius: 50%; background: #333; }
</style>
</head>
<body>
  <div class="page-band"></div>

  <header>
    <a class="brand" href="#"><span class="brand-dot"></span><span class="brand-name">LOMVI</span></a>
    <div class="search">
      <span class="search-input">Search here..</span>
      <span class="search-btn"><svg width="6" height="9" viewBox="0 0 6 9"><path d="M0 0 L6 4.5 L0 9Z" fill="#b0b0b0"/></svg></span>
    </div>
    <nav class="main-nav">
      <a href="#">Home</a><a href="#">Products</a><a href="#">News</a><a href="#">Contact</a>
    </nav>
  </header>

  <section class="hero">
    <div class="hero-photo" role="img" aria-label="Road worker in a hard hat and high-visibility jacket using a tablet on a gravel construction site">
      <div class="hero-panel">
        <div class="hero-kicker">Cloud-based Service for</div>
        <div class="hero-title">Road Construction</div>
        <p>Morbi porta, libero id ullamcorper nonummy, nibh ligula Ut nisi erat, fermentum vel, congue id, euismod in, elit.</p>
        <p>Mauris neque metus, malesuada nec, ultricies sit amet, porttitor mattis, enim. In massa libero, interdum nec, interdum vel, blandit sed, nulla. In ullamcorper, est eget tempor cursus, neque mi consectetuer</p>
        <a class="hero-cta" href="#">Learn More</a>
        <div class="hero-dots"><span></span><span></span><span></span><span></span></div>
      </div>
    </div>
  </section>

  <main>
    <section class="latest">
      <h2 class="section-title">Latest News</h2>
      <article class="news-item">
        <div class="news-thumb"><div class="thumb-workers" role="img" aria-label="Construction workers in hard hats at a rocky quarry"></div></div>
        <div class="news-body">
          <h3 class="news-headline">News Headline goes here</h3>
          <p>Fusce tellus. Sed metus augue, convallis et, vehicula ut, pulvinar eu, ante. Integer orci tellus, tristique vitae, consequat nec, porta vel, lectus. Nulla sit amet diam.</p>
          <p>Duis non nunc. Nulla rhoncus dictum metus. Curabitur tristique mi condimentum orci. Phasellus pellentesque aliquam enim. Proin dui lectus, cursus eu, mattis laoreet, viverra sit amet, quam. Curabitur vel dolor ultrices ipsum dictum tristique. Praesent vitae lacus. Ut velit enim, vestibulum non, fermentum nec, hendrerit quis, leo. Pellentesque rutrum malesuada neque.</p>
          <a class="more" href="#">LEARN MORE</a>
        </div>
      </article>
      <article class="news-item">
        <div class="news-thumb"><div class="thumb-bridge" role="img" aria-label="Elevated highway bridge seen from below against a blue sky"></div></div>
        <div class="news-body">
          <h3 class="news-headline">News Headline goes here</h3>
          <p>Fusce tellus. Sed metus augue, convallis et, vehicula ut, pulvinar eu, ante. Integer orci tellus, tristique vitae, consequat nec, porta vel, lectus. Nulla sit amet diam.</p>
          <p>Duis non nunc. Nulla rhoncus dictum metus. Curabitur tristique mi condimentum orci. Phasellus pellentesque aliquam enim. Proin dui lectus, cursus eu, mattis laoreet, viverra sit amet, quam. Curabitur vel dolor ultrices ipsum dictum tristique. Praesent vitae lacus. Ut velit enim, vestibulum non, fermentum nec, hendrerit quis, leo. Pellentesque rutrum malesuada neque.</p>
          <a class="more" href="#">LEARN MORE</a>
        </div>
      </article>
      <article class="news-item">
        <div class="news-thumb"><div class="thumb-site" role="img" aria-label="Site engineer in a hard hat in front of an excavator"></div></div>
        <div class="news-body">
          <h3 class="news-headline">News Headline goes here</h3>
          <p>Fusce tellus. Sed metus augue, convallis et, vehicula ut, pulvinar eu, ante. Integer orci tellus, tristique vitae, consequat nec, porta vel, lectus. Nulla sit amet diam.</p>
          <p>Duis non nunc. Nulla rhoncus dictum metus. Curabitur tristique mi condimentum orci. Phasellus pellentesque aliquam enim. Proin dui lectus, cursus eu, mattis laoreet, viverra sit amet, quam. Curabitur vel dolor ultrices ipsum dictum tristique.</p>
          <a class="more" href="#">LEARN MORE</a>
        </div>
      </article>
    </section>

    <div class="divider"></div>

    <aside class="viewed">
      <h2 class="section-title">Most Viewed News</h2>
      <div class="viewed-item">
        <div class="viewed-date">20.Nov.2012</div>
        <p>Mauris vel lacus vitae felis vestibulum volutpat. Etiam est nunc, venenatis in, tristique eu, imperdiet ac, nisl. Cum sociis natoque penatibus et magnis dis</p>
        <a class="more" href="#">LEARN MORE</a>
      </div>
      <div class="viewed-item">
        <div class="viewed-date">02.Nov.2012</div>
        <p>Mauris vel lacus vitae felis vestibulum volutpat. Etiam est nunc, venenatis in, tristique eu, imperdiet ac, nisl. Cum sociis natoque penatibus et magnis dis</p>
        <a class="more" href="#">LEARN MORE</a>
      </div>
      <div class="viewed-item">
        <div class="viewed-date">15.Oct.2012</div>
        <p>Mauris vel lacus vitae felis vestibulum volutpat. Etiam est nunc, venenatis in, tristique eu, imperdiet ac, nisl. Cum sociis natoque penatibus et magnis dis</p>
        <a class="more" href="#">LEARN MORE</a>
      </div>
      <div class="viewed-item">
        <div class="viewed-date">05.Oct.2012</div>
        <p>Mauris vel lacus vitae felis vestibulum volutpat. Etiam est nunc, venenatis in, tristique eu, imperdiet ac, nisl. Cum sociis natoque penatibus et magnis dis</p>
        <a class="more" href="#">LEARN MORE</a>
      </div>
    </aside>
  </main>

  <footer class="site-footer">
    <div class="copyright">© 2012 Company Name.&nbsp; All right reserved.&nbsp; Term of Use</div>
    <div class="touch">Get In Touch <span class="touch-circle"></span><span class="touch-circle"></span><span class="touch-circle"></span></div>
  </footer>
</body>
</html>
```